Modern Quillby Tree Care Website

I need a website for a full service Tree Care company. The company provides tree pruning, tree removal, tree preservation, emergency services, stump grinding, and emergency tree services.

Target Market(s)

Customers that need tree services

Industry/Entity Type

Landscaping, Tree Services

Coding

Coded - Design and coding required

Number of Pages Required

5+ page

Font styles to use
Sans Serif

Requirements
Must have
• Good clean design that showcases the services the company provides.
Nice to have
• Services page; contact form, blog, home page, about page

```html
<!DOCTYPE html>
<html lang="en">
<head>
<meta charset="utf-8">
<title>Quillby Tree Care</title>
<link href="https://fonts.googleapis.com/css2?family=Montserrat:wght@400;500;600;700&family=Jost:wght@400;500;600&display=swap" rel="stylesheet">
<style>
:root{
  --green:#7ac143;
  --green-deep:#4a9a3a;
  --forest:#3e5e2c;
  --night:#13241a;
  --orange:#f5a623;
  --ink:#1d1d1d;
  --muted:#6b6b6b;
  --mist:#f2f6ea;
  --card:#eef0e6;
  --line:#d9e3cc;
}
*{margin:0;padding:0;box-sizing:border-box}
html,body{width:1200px;height:1200px;overflow:hidden;background:#fff}
body{font-family:'Jost',sans-serif;color:var(--ink);position:relative}
.page{position:absolute;left:486px;top:14px;width:1440px;height:7376px;transform:scale(.1585);transform-origin:0 0;background:#fff;box-shadow:0 0 60px rgba(0,0,0,.12);overflow:hidden}
.abs{position:absolute}
h1,h2,h3,.heading{font-family:'Montserrat',sans-serif;font-weight:500;color:var(--ink)}
.eyebrow{font-size:15px;color:var(--green);display:flex;align-items:center;gap:14px}
.eyebrow::after{content:"";width:90px;height:2px;background:var(--green)}
.section-title{font-size:44px;line-height:1.25;font-weight:600}
.body-copy{font-size:15px;line-height:1.7;color:var(--muted)}
.btn{display:inline-block;border-radius:40px;font-size:14px;font-weight:500;padding:12px 30px}
.btn-solid{background:var(--green);color:#fff}
.btn-ghost{border:2px solid var(--green);color:var(--ink)}
.btn-orange-ghost{border:2px solid var(--orange);color:var(--ink)}
/* nav */
.hero-bg{left:0;top:0;width:1440px;height:880px;background:linear-gradient(160deg,#f6f9ef 0%,#eef5e2 60%,#fff 100%)}
.logo{left:125px;top:42px;display:flex;align-items:center;gap:10px;font-family:'Montserrat',sans-serif;font-weight:700;font-size:30px;color:var(--forest)}
.logo span.mark{width:34px;height:34px;background:var(--green)}
.nav{left:620px;top:56px;display:flex;gap:44px;font-size:16px}
.nav .active{color:var(--orange)}
.nav-cta{left:1164px;top:42px}
/* hero */
.hero-title{left:125px;top:220px;font-size:56px;line-height:1.18;font-weight:400}
.hero-title b{font-weight:700}
.hero-title em{font-style:normal;color:var(--green);font-weight:600}
.hero-text{left:125px;top:440px;width:480px}
.hero-btns{left:125px;top:555px;display:flex;gap:18px}
.hero-photo{left:892px;top:133px;width:423px;height:578px;background:linear-gradient(135deg,#8aa56a,#c9a66b 55%,#3f5a2a)}
.hero-photo-sm{left:770px;top:510px;width:180px;height:255px;background:linear-gradient(180deg,#6d8f3f,#2f4a22)}
.play{left:745px;top:530px;width:70px;height:70px;border-radius:50%;background:var(--green);border:8px solid #e7f3d9}
.ghost-word{font-family:'Montserrat',sans-serif;font-weight:700;color:rgba(122,193,67,.18)}
/* process */
.process-cards .card{position:absolute;top:1076px;width:280px;height:372px;background:linear-gradient(160deg,var(--card) 60%,#f7ead8);text-align:center;padding-top:60px}
.icon-ring{width:110px;height:110px;border-radius:50%;border:2px dashed var(--line);margin:0 auto 30px;display:flex;align-items:center;justify-content:center}
.icon-ring i{width:84px;height:84px;border-radius:50%;background:var(--green)}
.icon-ring.orange i{background:var(--orange)}
.card h3{font-size:19px;font-weight:500;line-height:1.3}
.card p{font-size:13px;color:var(--muted);margin-top:30px;line-height:1.6;padding:0 30px}
/* about */
.about-a{left:135px;top:1596px;width:320px;height:310px;border-radius:0 0 160px 160px;background:linear-gradient(135deg,#4a6b2e,#9a7a52)}
.about-b{left:475px;top:1596px;width:180px;height:494px;border-radius:90px;background:linear-gradient(180deg,#4f7d3a,#1f3a1c)}
.about-blob{left:135px;top:1925px;width:320px;height:165px;border-radius:90px;background:#d6f4ae}
/* services */
.svc-title{font-size:22px;font-weight:500}
.svc-num{font-family:'Montserrat',sans-serif;font-size:70px;font-weight:700;color:rgba(122,193,67,.15);position:absolute;top:-50px;left:-18px}
.readmore{font-size:12px;color:var(--green);margin-top:14px}
/* cta */
.cta{left:0;top:3201px;width:1440px;height:595px;background:var(--forest)}
.cta-title{left:128px;top:3490px;font-size:42px;line-height:1.3;color:#fff;font-weight:500}
.phones{font-family:'Montserrat',sans-serif;font-size:30px;font-weight:600;color:#fff;line-height:1.5}
/* choose */
.ticks{display:grid;grid-template-columns:380px 300px;gap:22px 0;font-size:17px;color:var(--ink)}
/* testimonial */
.quote-card{left:356px;top:4645px;width:712px;height:403px;background:#e9f0dc}
.dots{display:flex;gap:10px}
.dots i{width:12px;height:12px;border-radius:50%;border:2px solid #777}
.dots i.on{background:#333;border-color:#333}
/* blog */
.post{position:absolute;top:5369px;width:384px}
.post .img{height:250px}
.post small{display:block;font-size:11px;color:var(--orange);margin-top:24px}
.post h4{font-family:'Montserrat',sans-serif;font-size:20px;font-weight:500;margin-top:8px;line-height:1.4}
.post p{font-size:12px;color:var(--muted);margin-top:10px;line-height:1.6}
/* contact */
.form{left:732px;top:5999px;width:540px;height:669px;background:var(--green-deep);padding:70px 60px;z-index:2}
.field{border-bottom:1px solid rgba(255,255,255,.55);color:#fff;font-size:14px;padding-bottom:24px;margin-bottom:48px}
.field.message{padding-bottom:70px}
/* footer */
.footer{left:0;top:6660px;width:1440px;height:716px;background:linear-gradient(180deg,#ffffff 0%,#b8cda1 12%,#3d5a2c 38%,#13241a 70%,#0c1811 100%)}
.foot-head{font-family:'Montserrat',sans-serif;color:#fff;font-size:22px;font-weight:500}
.foot-links{font-size:14px;color:#d8e3cf;line-height:2.5;margin-top:20px}
</style>
</head>
<body>
<div class="page">
  <div class="abs hero-bg"></div>
  <div class="abs logo"><span class="mark"></span>QUILLBY</div>
  <nav class="abs nav"><span class="active">Home</span><span>About Us</span><span>Services</span><span>Blog</span><span>Contact Us</span></nav>
  <span class="abs btn btn-solid nav-cta">Get A Quote</span>

  <h1 class="abs hero-title">Professional <em>Garden</em><br>&amp; <b>Landscaping</b><br>Services</h1>
  <p class="abs body-copy hero-text">At Quillby Tree Care, we are more than just a tree service company, we are stewards of our beautiful trees. With a passion deeply rooted in arboriculture.</p>
  <div class="abs hero-btns"><span class="btn btn-solid">Consult Us</span><span class="btn btn-ghost">Our Services</span></div>
  <div class="abs hero-photo" role="img" aria-label="Photo of a gardener tending a potted lemon tree"></div>
  <div class="abs hero-photo-sm" role="img" aria-label="Photo of hands trimming a green hedge"></div>
  <div class="abs play"></div>
  <div class="abs ghost-word" style="left:770px;top:520px;font-size:64px;transform:rotate(-90deg);transform-origin:left top">QUILLBY</div>
  <div class="abs ghost-word" style="left:970px;top:710px;font-size:52px">TREE CARE</div>

  <!-- process -->
  <div class="abs eyebrow" style="left:129px;top:880px">Our Work Process</div>
  <h2 class="abs section-title" style="left:129px;top:915px">See How We Complete<br>The Work</h2>
  <p class="abs body-copy" style="left:808px;top:925px;width:505px">Lorem ipsum dolor sit amet, consectetur adipiscing elit. Donec finibus lorem sed ultricies aliquam. Donec non libero eget risus aliquam luctus. Quisque placerat orci ac sagittis egestas.</p>
  <div class="process-cards">
    <div class="card" style="left:129px"><div class="icon-ring"><i></i></div><h3>Gardening and<br>Landscaping</h3><p>Suspendisse finibus, magna sed dictum semper, lacus.</p></div>
    <div class="card" style="left:429px"><div class="icon-ring orange"><i></i></div><h3>Planting</h3><p>Suspendisse finibus, magna sed dictum semper, lacus.</p></div>
    <div class="card" style="left:732px"><div class="icon-ring"><i></i></div><h3>Garden<br>Maintenance</h3><p>Suspendisse finibus, magna sed dictum semper, lacus.</p></div>
    <div class="card" style="left:1033px"><div class="icon-ring"><i></i></div><h3>Renovations<br>Inside + Outside</h3><p>Suspendisse finibus, magna sed dictum semper, lacus.</p></div>
  </div>

  <!-- about -->
  <div class="abs about-a" role="img" aria-label="Photo of an arborist sawing a branch"></div>
  <div class="abs about-b" role="img" aria-label="Photo of a worker trimming hedge with shears"></div>
  <div class="abs about-blob"></div>
  <div class="abs eyebrow" style="left:751px;top:1630px">About Us</div>
  <h2 class="abs section-title" style="left:751px;top:1668px;font-size:42px">About Quillby Tree Care</h2>
  <div class="abs body-copy" style="left:751px;top:1745px;width:510px;font-size:14px">
    <p>At Quillby Tree Care, we are more than just a tree service company, we are stewards of our beautiful trees. With a passion deeply rooted in arboriculture, we embark on a mission to promote the health, beauty, and safety of your trees and landscapes.</p>
    <p style="margin-top:22px">Whether it's expert tree trimming to enhance aesthetics, meticulous tree removal to mitigate hazards, or comprehensive tree health assessments to ensure safety, we approach each task with unwavering dedication and attention to detail.</p>
  </div>
  <span class="abs btn btn-orange-ghost" style="left:751px;top:2020px">Learn More</span>

  <!-- services -->
  <div class="abs eyebrow" style="left:129px;top:2222px">Our Services</div>
  <h2 class="abs section-title" style="left:129px;top:2258px">We Provide<br>the Best Services</h2>
  <p class="abs body-copy" style="left:808px;top:2268px;width:505px">Lorem ipsum dolor sit amet, consectetur adipiscing elit. Donec finibus lorem sed ultricies aliquam. Donec non libero eget risus aliquam luctus. Quisque placerat orci ac sagittis egestas.</p>
  <span class="abs btn btn-ghost" style="left:808px;top:2365px">View All Services</span>

  <div class="abs" style="left:172px;top:2440px;width:300px"><span class="svc-num">01</span><h3 class="svc-title">Tree Pruning</h3><p class="body-copy" style="font-size:13px;margin-top:10px">Lorem ipsum dolor sit amet, consectetur adipiscing elit. Cras quis congue ipsum. Nullam eget hendrerit odio...</p><div class="readmore">Read More →</div></div>
  <div class="abs" style="left:172px;top:2637px;width:294px;height:388px;background:linear-gradient(160deg,#8a6a4e,#c8c0b2 50%,#6b7f4c)" role="img" aria-label="Photo of gloved hands pruning branches"></div>

  <div class="abs" style="left:579px;top:2700px;width:300px"><span class="svc-num">02</span><h3 class="svc-title">Tree Removal</h3><p class="body-copy" style="font-size:13px;margin-top:10px">Lorem ipsum dolor sit amet, consectetur adipiscing elit. Cras quis congue ipsum. Nullam eget hendrerit odio...</p><div class="readmore">Read More →</div></div>
  <div class="abs" style="left:579px;top:2888px;width:298px;height:395px;background:linear-gradient(160deg,#3d6b2b,#c9a677 45%,#2e4b22)" role="img" aria-label="Photo of a chainsaw cutting a log"></div>

  <div class="abs" style="left:978px;top:2520px;width:300px"><span class="svc-num">03</span><h3 class="svc-title">Tree Preservation</h3><p class="body-copy" style="font-size:13px;margin-top:10px">Lorem ipsum dolor sit amet, consectetur adipiscing elit. Cras quis congue ipsum. Nullam eget hendrerit odio...</p><div class="readmore">Read More →</div></div>
  <div class="abs" style="left:978px;top:2716px;width:294px;height:387px;background:radial-gradient(circle at 50% 40%,#7fb04a,#2f4a22 70%)" role="img" aria-label="Photo of hands holding a young tree with its root ball"></div>

  <!-- call to action -->
  <div class="abs cta"></div>
  <h2 class="abs cta-title">Call QUILLBY for All Your<br>Tree Care Needs</h2>
  <span class="abs btn" style="left:128px;top:3640px;background:#fff;color:var(--ink)">Consult Us</span>
  <div class="abs" style="left:824px;top:3470px;width:460px;color:#fff">
    <p style="font-size:17px;line-height:1.5">Call us today to see how we can help you with all of your tree needs:</p>
    <p style="font-size:13px;line-height:1.7;margin-top:14px;color:#d7e4cc">Lorem ipsum dolor sit amet, consectetur adipiscing elit. Cras quis congue ipsum. Nullam eget hendrerit odio, sit amet ultricies diam. Curabitur diam erat, venenatis id iaculis sit amet.</p>
    <div style="display:flex;gap:20px;margin-top:26px;align-items:center">
      <svg width="54" height="54" viewBox="0 0 24 24" fill="none" stroke="#f5a623" stroke-width="1.5"><path d="M5 3h4l2 5-2.5 1.5a11 11 0 0 0 6 6L16 13l5 2v4a2 2 0 0 1-2 2A16 16 0 0 1 3 5a2 2 0 0 1 2-2z"/></svg>
      <div class="phones">(555) 214-3087<br>(555) 390-6642</div>
    </div>
  </div>

  <!-- why choose -->
  <div class="abs eyebrow" style="left:129px;top:3935px">People Love</div>
  <h2 class="abs section-title" style="left:129px;top:3975px">They Choose Us</h2>
  <p class="abs body-copy" style="left:129px;top:4045px;width:500px;font-size:14px">People choose our team because our arborists are the face of the company, well trained in sharing great stories and accurate information for your benefit.</p>
  <div class="abs ticks" style="left:129px;top:4150px">
    <span>- Licensed and Insured</span><span>- Safety is Our No.1 Priority</span>
    <span>- 24-Hours Emergency Services</span><span>- Free Estimates</span>
    <span>- Locally Owned &amp; Operated</span><span>- Licensed Arborist on Staff</span>
    <span>- Professional Work</span><span></span>
  </div>
  <div class="abs" style="left:872px;top:3923px;width:150px;height:260px;border-radius:75px;background:linear-gradient(180deg,#6a8a4a,#2d3f24)" role="img" aria-label="Photo of hands planting a seedling"></div>
  <div class="abs" style="left:1035px;top:3923px;width:280px;height:390px;border-radius:0 0 140px 140px;background:linear-gradient(160deg,#8fb05e,#b5764a 60%,#4b6a30)" role="img" aria-label="Photo of a gardener with potted citrus plants"></div>
  <div class="abs" style="left:893px;top:4200px;width:110px;height:110px;border-radius:50%;background:#fde3b8"></div>

  <!-- testimonials -->
  <div class="abs eyebrow" style="left:560px;top:4465px;width:320px;justify-content:center">Testimonials</div>
  <h2 class="abs section-title" style="left:0;top:4500px;width:1440px;text-align:center;font-size:40px">Customer Feedback</h2>
  <div class="abs quote-card"></div>
  <div class="abs" style="left:400px;top:4640px;font-family:'Montserrat',sans-serif;font-size:90px;font-weight:700;color:var(--green);line-height:1">“</div>
  <div class="abs body-copy" style="left:432px;top:4730px;width:480px;font-size:17px;color:#333">
    <p>Lorem ipsum dolor sit amet, consectetur adipiscing elit. Ut quis ipsum vitae neque efficitur vestibulum nec eu mi. Etiam ex ipsum, faucibus eu ornare a, congue eu magna. Quisque sit amet rutrum massa, eu gravida massa.</p>
    <p style="margin-top:20px">Vestibulum quis enim at turpis auctor feugiat. Vestibulum efficitur vulputate risus elementum suscipit.</p>
  </div>
  <div class="abs" style="left:985px;top:4756px;width:190px;height:185px;background:linear-gradient(160deg,#8a8f96,#3c4654);border:5px solid #fff" role="img" aria-label="Portrait photo of the customer"></div>
  <div class="abs" style="left:1005px;top:4955px"><div style="font-size:20px;font-family:'Montserrat',sans-serif">Dana Holt</div><div style="font-size:11px;color:var(--muted)">Customer</div></div>
  <div class="abs dots" style="left:656px;top:5110px"><i></i><i></i><i class="on"></i><i></i><i></i></div>

  <!-- blog -->
  <div class="abs eyebrow" style="left:560px;top:5230px;width:320px;justify-content:center">Our Articles</div>
  <h2 class="abs section-title" style="left:0;top:5265px;width:1440px;text-align:center;font-size:40px">Latest Blog Post</h2>
  <div class="post" style="left:117px"><div class="img" style="background:linear-gradient(160deg,#6b8f3a,#7a5a3c)" role="img" aria-label="Photo of hands planting a seedling in soil"></div><small>14th Nov, 2023</small><h4>Lorem ipsum dolor sit amet, consectetur...</h4><p>Lorem ipsum dolor sit amet, consectetur adipiscing elit, sed do eiusmod tempor [...]</p><div class="readmore">— Read More</div></div>
  <div class="post" style="left:520px"><div class="img" style="background:linear-gradient(160deg,#7aa34a,#b0854a 60%,#4c6d2c)" role="img" aria-label="Photo of a gardener mowing grass"></div><small>14th Nov, 2023</small><h4>Lorem ipsum dolor sit amet, consectetur...</h4><p>Lorem ipsum dolor sit amet, consectetur adipiscing elit, sed do eiusmod tempor [...]</p><div class="readmore">— Read More</div></div>
  <div class="post" style="left:922px"><div class="img" style="background:linear-gradient(160deg,#4d6a34,#8a6b4a 60%,#3b3a2c)" role="img" aria-label="Photo of garden tools beside flowers"></div><small>14th Nov, 2023</small><h4>Lorem ipsum dolor sit amet, consectetur...</h4><p>Lorem ipsum dolor sit amet, consectetur adipiscing elit, sed do eiusmod tempor [...]</p><div class="readmore">— Read More</div></div>
  <div class="abs" style="left:686px;top:5870px;display:flex;gap:8px"><i style="width:14px;height:3px;background:#ccc"></i><i style="width:14px;height:3px;background:var(--orange)"></i><i style="width:14px;height:3px;background:#ccc"></i></div>

  <!-- footer -->
  <div class="abs footer" role="img" aria-label="Photo of tall green grass against a dark sky"></div>
  <h2 class="abs" style="left:125px;top:7000px;font-size:46px;line-height:1.35;color:#fff;font-weight:400">Let's Build Something<br>Amazing Together</h2>
  <p class="abs" style="left:125px;top:7165px;color:#fff;font-size:16px;line-height:1.8">Making a fairy garden! Get design free!<br>Or call us: (555) 214-3087 / (555) 390-6642</p>
  <div class="abs" style="left:832px;top:6995px"><div class="foot-head">Quick Links</div><div class="foot-links">Home<br>About us<br>Services<br>Blog<br>Contact us</div></div>
  <div class="abs" style="left:1090px;top:6995px"><div class="foot-head">Address</div><div class="foot-links" style="line-height:1.9">27 Alder Lane, Brookvale,<br>NR 4402<br><br>hello@quillbytrees.example</div></div>
  <div class="abs" style="left:125px;top:7308px;width:700px;height:1px;background:rgba(255,255,255,.3)"></div>
  <p class="abs" style="left:880px;top:7298px;color:#d8e3cf;font-size:14px">Copyright © 2024 <span style="color:var(--orange)">Quillby Tree Care</span>. All rights reserved.</p>

  <!-- contact -->
  <div class="abs eyebrow" style="left:184px;top:5995px">Get In Touch</div>
  <h2 class="abs section-title" style="left:184px;top:6030px;font-size:40px">Contact Us</h2>
  <div class="abs" style="left:164px;top:6124px;width:544px;height:536px;background:linear-gradient(160deg,#9aa38a,#4b5a3a 60%,#c9b24a);z-index:2" role="img" aria-label="Photo of two women tending flowers in a greenhouse"></div>
  <div class="abs form">
    <div class="field">Full Name</div>
    <div class="field">Phone Number</div>
    <div class="field">Email Address</div>
    <div class="field">Services</div>
    <div class="field message">Message Here</div>
    <span class="btn" style="background:var(--orange);color:#fff">Send Message</span>
  </div>
</div>
</body>
</html>
```